Post Card Mailer Design for targeted consumers, real estate professionals and renters

I would like to have a design that is readily for post cards/flyers that will be sent out for mass mailings, address of location that coupon is being honored is located at 4817-226 Larkspur Bend Road, Raleigh, NC 27655 and NEW LOCATION that the store is moving to is 7293 Maple Crest Road, Raleigh, NC 27688. Please see the revised Microsoft Word document for reference.

Target Market(s)

Consumers, renters, homeowners

Industry/Entity Type

real estate, shipping, packaging, renters

Font styles to use
Sans Serif

Colors
0054AA
0677BA
7BADD7
CADEEF
E8F1F8
FFF300
FFF600
FEFA6F
FFFEC7
FFFEE8
EB3D1F
EC4F4E
F09395
F8D3D4
FCEDEE

Requirements
Must have
• vibrant colors, preferrably red, blue yellow, white
Nice to have
• fun and creative and must get the information out with the coupon that has the document attached.
Should not have
• must be readable and not clunky

```html
<!DOCTYPE html>
<html lang="en">
<head>
<meta charset="utf-8">
<title>Brisk Box and Mail – Postcard Mailer</title>
<link href="https://fonts.googleapis.com/css2?family=Montserrat:wght@400;500;600;700;800;900&display=swap" rel="stylesheet">
<style>
  :root{
    --blue:#0054AA;
    --blue-mid:#0677BA;
    --blue-soft:#CADEEF;
    --blue-row:#E8F1F8;
    --red:#EC4F4E;
    --red-deep:#EB3D1F;
    --pink-row:#FCEDEE;
    --yellow:#FFF600;
    --yellow-soft:#FEFA6F;
    --ink:#1d1d1f;
    --paper:#ffffff;
    --stage:#5e5e5e;
    --kraft:#d2aa7c;
    --kraft-light:#e8cba3;
    --maroon:#6b1a1f;
  }
  *{box-sizing:border-box;margin:0;padding:0}
  html,body{width:1200px;height:900px;overflow:hidden}
  body{background:var(--stage);font-family:"Montserrat",sans-serif;color:var(--ink);position:relative}

  .card{position:absolute;width:585px;height:390px;background:var(--paper);top:255px}
  .card--services{left:10px;padding:10px}
  .card--coupon{left:605px}

  /* ---------- services side ---------- */
  .services__header{background:var(--red);color:#fff;font-weight:800;font-size:14.5px;line-height:1.2;padding:10px 14px;height:60px}
  .services__grid{display:grid;grid-template-columns:repeat(9,1fr);border-left:1px solid #9aa7b4}
  .services__col{display:flex;flex-direction:column;border-right:1px solid #9aa7b4}
  .services__title{background:var(--blue);color:#fff;font-weight:700;font-size:6.6px;line-height:1.15;height:28px;display:flex;align-items:center;padding:0 4px}
  .services__item{height:21px;font-size:6.4px;line-height:1.1;font-weight:500;padding:0 4px;display:flex;align-items:center;border-bottom:1px solid #a9b5c0}
  .services__item:nth-child(even){background:var(--blue-row)}
  .services__item:nth-child(odd){background:var(--pink-row)}
  .services__footer{background:var(--blue);color:#fff;height:30px;display:flex;align-items:center;justify-content:space-around;font-size:11px;font-weight:500}
  .contact-line{display:flex;align-items:center;gap:5px}
  .icon{width:12px;height:12px;flex:none}

  /* ---------- coupon side ---------- */
  .stamp-box{position:absolute;top:14px;right:16px;width:68px;height:60px;border:1px solid #777}
  .return-address{position:absolute;top:44px;left:318px;font-size:8.5px;line-height:1.25}
  .return-address strong{font-weight:700;display:block}
  .address-line{position:absolute;left:340px;width:225px;border-top:1px solid #888}
  .coupon-tab{position:absolute;top:62px;left:16px;background:var(--blue);color:#fff;font-weight:800;font-size:12px;padding:4px 12px;border-radius:4px}
  .coupon{position:absolute;left:16px;width:330px;height:56px;display:flex;border-radius:5px;overflow:hidden}
  .coupon--shipping{top:86px}
  .coupon--retail{top:150px}
  .coupon__value{background:var(--blue-mid);color:#fff;width:82px;display:flex;align-items:center;justify-content:center;border:1.5px dashed #fff;outline:3px solid var(--blue-mid)}
  .coupon__num{font-size:30px;font-weight:800;line-height:1}
  .coupon__unit{font-size:11px;font-weight:800;line-height:1;margin-left:2px}
  .coupon__text{flex:1;background:var(--red);color:#fff;font-weight:800;font-size:11.5px;line-height:1.3;padding:0 12px;display:flex;flex-direction:column;justify-content:center;border:1.5px dashed #fff;outline:3px solid var(--red)}
  .mailbox-offer{position:absolute;top:214px;left:18px;line-height:1.2}
  .mailbox-offer__lead{font-size:14px;font-weight:800;color:var(--blue)}
  .mailbox-offer__lead em{font-style:normal;color:var(--red-deep)}
  .mailbox-offer__note{font-size:10.5px;font-weight:800}
  .valid-bar{position:absolute;top:258px;left:30px;display:flex;height:22px;font-weight:800;font-size:10.5px;z-index:1}
  .valid-bar__label{background:var(--red-deep);color:#fff;padding:0 10px;display:flex;align-items:center;border-radius:4px 0 0 4px}
  .valid-bar__date{background:var(--yellow-soft);padding:0 12px;display:flex;align-items:center;border:1px solid var(--red-deep);border-radius:0 4px 4px 0}
  .contact-panel{position:absolute;top:288px;left:60px;width:340px;height:82px;background:var(--blue);border-radius:6px;color:#fff;display:flex;justify-content:space-between;align-items:flex-end;padding:10px 14px;font-size:9.5px}
  .contact-panel__list{display:flex;flex-direction:column;gap:3px}
  .contact-panel__social{display:flex;flex-direction:column;gap:4px;align-self:flex-start;margin-top:8px}
  .social-mark{width:10px;height:10px;background:#fff;border-radius:2px;flex:none}
  .parcel-photo{position:absolute;left:420px;top:262px;width:96px;height:74px;background:linear-gradient(135deg,var(--kraft-light),var(--kraft));border-radius:3px}
  .brand-mark{position:absolute;right:20px;bottom:48px;display:flex;align-items:center;gap:6px;color:var(--maroon);font-weight:700;font-size:13px}
  .brand-mark__dot{width:12px;height:12px;border-radius:50%;background:var(--maroon)}
</style>
</head>
<body>

<section class="card card--services">
  <header class="services__header">
    Fast and Friendly service for all your shipping and printing needs<br>
    Mailing, Printing, Gifts, Cards &amp; Printing Solutions.
  </header>

  <div class="services__grid">
    <div class="services__col">
      <div class="services__title">Shipping</div>
      <div class="services__item">AirSwift</div>
      <div class="services__item">ParcelJet</div>
      <div class="services__item">GroundLine</div>
      <div class="services__item">National Post</div>
      <div class="services__item">Postage Stamps</div>
      <div class="services__item">Packaging Supplies</div>
      <div class="services__item">Artwork Shipping</div>
      <div class="services__item"></div>
      <div class="services__item"></div>
      <div class="services__item"></div>
    </div>
    <div class="services__col">
      <div class="services__title">Print-Copy-Scan</div>
      <div class="services__item">Blueprint Scanning</div>
      <div class="services__item">Poster and Banner Printing</div>
      <div class="services__item">Document Scaning</div>
      <div class="services__item"></div>
      <div class="services__item"></div>
      <div class="services__item"></div>
      <div class="services__item"></div>
      <div class="services__item"></div>
      <div class="services__item"></div>
      <div class="services__item"></div>
    </div>
    <div class="services__col">
      <div class="services__title">Home &amp; Business</div>
      <div class="services__item">Document Shredding</div>
      <div class="services__item">eBoxly Virtual Mailboxes</div>
      <div class="services__item">Mailbox Rental</div>
      <div class="services__item">Notary Public</div>
      <div class="services__item">Key Duplication</div>
      <div class="services__item">Passport Photos</div>
      <div class="services__item">Neighborhood Direct Mail</div>
      <div class="services__item">Computer Rental</div>
      <div class="services__item"></div>
      <div class="services__item"></div>
    </div>
    <div class="services__col">
      <div class="services__title">Canvas &amp; Aluminum Prints</div>
      <div class="services__item">Watercolor Paper</div>
      <div class="services__item">Semi-gloss Photo Paper</div>
      <div class="services__item">Yard Signs</div>
      <div class="services__item"></div>
      <div class="services__item"></div>
      <div class="services__item"></div>
      <div class="services__item"></div>
      <div class="services__item"></div>
      <div class="services__item"></div>
      <div class="services__item"></div>
    </div>
    <div class="services__col">
      <div class="services__title">Business Cards</div>
      <div class="services__item">Business Card Design Services</div>
      <div class="services__item">Paper Selection</div>
      <div class="services__item">Customer card, shapes and styles</div>
      <div class="services__item">Full-color</div>
      <div class="services__item">Photo cards</div>
      <div class="services__item">Expedited services</div>
      <div class="services__item">Quantity Discounts</div>
      <div class="services__item">Fast &amp; Easy Reordering</div>
      <div class="services__item"></div>
      <div class="services__item"></div>
    </div>
    <div class="services__col">
      <div class="services__title">Photo Printing</div>
      <div class="services__item">Available in 4x6, 5x7 and 8x10</div>
      <div class="services__item">Same Day Pickup</div>
      <div class="services__item">Enlargement services</div>
      <div class="services__item">Print and Ship options</div>
      <div class="services__item">Glossy or Matte Finish</div>
      <div class="services__item"></div>
      <div class="services__item"></div>
      <div class="services__item"></div>
      <div class="services__item"></div>
      <div class="services__item"></div>
    </div>
    <div class="services__col">
      <div class="services__title">Document Finish/Binding</div>
      <div class="services__item">Collating</div>
      <div class="services__item">Stapling</div>
      <div class="services__item">Labeling</div>
      <div class="services__item">Binding</div>
      <div class="services__item">Presentation Covers</div>
      <div class="services__item">Specialty Papers</div>
      <div class="services__item">Laminating</div>
      <div class="services__item">Folding</div>
      <div class="services__item">Preparation for shipping</div>
      <div class="services__item"></div>
    </div>
    <div class="services__col">
      <div class="services__title">Copying Services</div>
      <div class="services__item">Single copies</div>
      <div class="services__item">Color copies</div>
      <div class="services__item">Collating</div>
      <div class="services__item">Binding</div>
      <div class="services__item">High-volume copies</div>
      <div class="services__item">Letter, legal, and ledger size</div>
      <div class="services__item">Stapling</div>
      <div class="services__item">Cutting</div>
      <div class="services__item">Black and white copies</div>
      <div class="services__item">Multiple paper options</div>
    </div>
    <div class="services__col">
      <div class="services__title">&nbsp;</div>
      <div class="services__item"></div>
      <div class="services__item"></div>
      <div class="services__item"></div>
      <div class="services__item"></div>
      <div class="services__item"></div>
      <div class="services__item"></div>
      <div class="services__item"></div>
      <div class="services__item"></div>
      <div class="services__item"></div>
      <div class="services__item"></div>
    </div>
  </div>

  <footer class="services__footer">
    <span class="contact-line">
      <svg class="icon" viewBox="0 0 24 24"><path fill="#fff" d="M6.6 10.8a15 15 0 0 0 6.6 6.6l2.2-2.2c.3-.3.7-.4 1-.2 1.1.4 2.3.6 3.6.6.6 0 1 .4 1 1V20c0 .6-.4 1-1 1A17 17 0 0 1 3 4c0-.6.4-1 1-1h3.5c.6 0 1 .4 1 1 0 1.3.2 2.5.6 3.6.1.3 0 .7-.2 1z"/></svg>
      919.555.0142
    </span>
    <span class="contact-line">
      <svg class="icon" viewBox="0 0 24 24"><rect x="2" y="5" width="20" height="14" rx="2" fill="#fff"/><path d="M3 6l9 7 9-7" stroke="#0054AA" stroke-width="2" fill="none"/></svg>
      hello@briskboxraleigh.com
    </span>
    <span class="contact-line">
      <svg class="icon" viewBox="0 0 24 24"><circle cx="12" cy="12" r="9" stroke="#fff" stroke-width="2" fill="none"/><path d="M3 12h18M12 3c3 3 3 15 0 18M12 3c-3 3-3 15 0 18" stroke="#fff" stroke-width="1.5" fill="none"/></svg>
      www.briskboxraleigh.com
    </span>
  </footer>
</section>

<section class="card card--coupon">
  <div class="stamp-box"></div>
  <address class="return-address" style="font-style:normal">
    <strong>BRISK BOX AND MAIL</strong>
    <strong>Willow Commons Center</strong>
    7293 Maple Crest Road<br>
    Raleigh, NC 27688
  </address>
  <div class="address-line" style="top:150px"></div>
  <div class="address-line" style="top:178px"></div>
  <div class="address-line" style="top:206px"></div>

  <div class="coupon-tab">SPECIALS COUPON:</div>

  <div class="coupon coupon--shipping">
    <div class="coupon__value"><span class="coupon__num">15</span><span class="coupon__unit">%<br>off</span></div>
    <div class="coupon__text"><span>any carriers being shipped</span><span>Min shipping order is $10</span></div>
  </div>

  <div class="coupon coupon--retail">
    <div class="coupon__value"><span class="coupon__num">20</span><span class="coupon__unit">%<br>off</span></div>
    <div class="coupon__text"><span>any retail/office items instore</span><span>Min item is $5</span></div>
  </div>

  <div class="mailbox-offer">
    <p class="mailbox-offer__lead">2 months <em>FREE</em> rent for any mailboxes</p>
    <p class="mailbox-offer__note">Must be 6 months, 12 months, or 15 months</p>
  </div>

  <div class="valid-bar">
    <span class="valid-bar__label">COUPON VALID</span>
    <span class="valid-bar__date">until September 30<sup style="font-size:6px">th</sup>&nbsp;2021</span>
  </div>

  <div class="contact-panel">
    <div class="contact-panel__list">
      <span class="contact-line">
        <svg class="icon" viewBox="0 0 24 24"><path fill="#fff" d="M6.6 10.8a15 15 0 0 0 6.6 6.6l2.2-2.2c.3-.3.7-.4 1-.2 1.1.4 2.3.6 3.6.6.6 0 1 .4 1 1V20c0 .6-.4 1-1 1A17 17 0 0 1 3 4c0-.6.4-1 1-1h3.5c.6 0 1 .4 1 1 0 1.3.2 2.5.6 3.6.1.3 0 .7-.2 1z"/></svg>
        919.555.0142
      </span>
      <span class="contact-line">
        <svg class="icon" viewBox="0 0 24 24"><rect x="2" y="5" width="20" height="14" rx="2" fill="#fff"/><path d="M3 6l9 7 9-7" stroke="#0054AA" stroke-width="2" fill="none"/></svg>
        hello@briskboxraleigh.com
      </span>
      <span class="contact-line">
        <svg class="icon" viewBox="0 0 24 24"><circle cx="12" cy="12" r="9" stroke="#fff" stroke-width="2" fill="none"/><path d="M3 12h18M12 3c3 3 3 15 0 18M12 3c-3 3-3 15 0 18" stroke="#fff" stroke-width="1.5" fill="none"/></svg>
        www.briskboxraleigh.com
      </span>
    </div>
    <div class="contact-panel__social">
      <span class="contact-line"><span class="social-mark"></span>Brisk Box Raleigh</span>
      <span class="contact-line"><span class="social-mark"></span>@briskboxral</span>
    </div>
  </div>

  <div class="parcel-photo" role="img" aria-label="Photo of stacked cardboard shipping boxes"></div>

  <div class="brand-mark"><span class="brand-mark__dot"></span>Brisk Box</div>
</section>

</body>
</html>
```